Indonesian B2B Company (Varo Ingredients) - Stationery Design

Varo Ingredients needs a corporate, bold and professional-looking stationery design.

Varo Ingredients is a new Indonesian company manufacturing, marketing and distributing various ingredients / raw materials such as flavours, fragrance, colours, sweeteners, preservatives for the food & beverage, pharmaceutical, personal care and other household goods industries.

It is a business to business (B2B) company as we supply various natural and synthetic raw materials to various consumer goods manufacturers. We therefore need a logo/identity with corporate and industrial style.

Varo Ingredients is a startup company which belongs to a larger Tumina Jaya group of companies (http://tuminajaya.bizplank.example/about) that focuses in the mining, petroleum and energy businesses. Varo Ingredients would like to focus in providing good quality, safe, reliable and affordable ingredients for the industries. Our tagline is "Quality Inputs for Industry"
Updates

We have updated some information including our requirements and contact details to be shown in the stationery. Please check the project brief.

Regards,

Varo Ingredients

Target Market(s)

Manufacturers of food & beverages, personal care, pharmaceutical and other FMCG factories.

Industry/Entity Type

Business

Requirements
Must have
• Smart, professional and corporate touches in the stationery designs. We require designs for:
1. Letterhead
2. Envelope (with and without window)
3. Name card
4. Powerpoint presentation template
5. CD label
6. Small memo / with compliments card

Contact details:

Company name:
PT Varo Ingredients

Address:
Ruko Pelita Sumber Asri, Blok K07 no: 15-16
Cempaka Hijau Utara, 14590
Indonesia

Tel:+62 21 738 2096
Fax:+62 21 738 2097
Email: info@varo-ingredients.example
Website: www.varo-ingredients.example

```html
<!DOCTYPE html>
<html lang="en">
<head>
<meta charset="utf-8">
<title>Varo Ingredients – Letterhead</title>
<link rel="stylesheet" href="https://fonts.googleapis.com/css2?family=Source+Sans+3:wght@400;600&display=swap">
<style>
  :root {
    --brand-red: #c1272d;
    --brand-red-light: #ee4a4a;
    --paper: #f6f6f7;
    --stage: #dcdddf;
    --ink: #2b2b2b;
    --muted: #8a8a8a;
    --white: #ffffff;
  }
  * { box-sizing: border-box; margin: 0; padding: 0; }
  html, body { width: 1200px; height: 960px; overflow: hidden; }
  body {
    background: var(--stage);
    font-family: "Source Sans 3", Arial, sans-serif;
    position: relative;
  }
  .letterhead {
    position: absolute;
    top: 98px;
    width: 540px;
    height: 764px;
    background: radial-gradient(circle at 55% 50%, var(--white) 0%, var(--paper) 70%, #ececed 100%);
    box-shadow: 0 6px 18px rgba(0,0,0,0.18);
    overflow: hidden;
  }
  .letterhead--wave { left: 40px; }
  .letterhead--rule { left: 620px; }
  .letterhead__art { position: absolute; inset: 0; width: 100%; height: 100%; }

  .brand { position: absolute; }
  .brand__name {
    color: var(--brand-red);
    font-size: 18px;
    font-weight: 400;
    letter-spacing: -0.2px;
    line-height: 1;
  }
  .brand__tagline {
    color: var(--muted);
    font-size: 8.5px;
    margin-top: 3px;
    line-height: 1;
  }
  .letterhead--wave .brand { left: 32px; top: 100px; }
  .letterhead--rule .brand { left: 0; right: 0; top: 96px; text-align: center; }

  .contact {
    position: absolute;
    font-size: 8.5px;
    line-height: 1.3;
    font-weight: 600;
    font-style: normal;
  }
  .letterhead--wave .contact { color: var(--white); }
  .letterhead--wave .contact--address { left: 30px; bottom: 16px; }
  .letterhead--wave .contact--lines { right: 18px; top: 668px; }
  .letterhead--rule .contact { color: var(--ink); }
  .letterhead--rule .contact--address { left: 14px; top: 706px; }
  .letterhead--rule .contact--lines { right: 20px; top: 706px; }
</style>
</head>
<body>

  <section class="letterhead letterhead--wave" aria-label="Letterhead with red wave bands">
    <svg class="letterhead__art" viewBox="0 0 540 764" aria-hidden="true">
      <path fill="var(--brand-red-light)" d="M0 0H540V150C532 122 515 114 480 114C380 116 270 128 190 134C176 70 140 34 96 34C52 34 18 54 0 76Z"/>
      <path fill="var(--brand-red)" d="M0 0H540V138C532 110 515 102 480 102C380 104 270 116 184 122C170 60 136 24 94 24C52 24 18 44 0 66Z"/>
      <path fill="var(--brand-red-light)" d="M0 764V648C10 690 40 700 90 695C250 680 380 628 480 618C510 615 530 618 540 623V764Z"/>
      <path fill="var(--brand-red)" d="M0 764V660C10 702 40 712 90 707C250 692 380 640 480 630C510 627 530 630 540 635V764Z"/>
    </svg>
    <div class="brand">
      <p class="brand__name">Varo Ingredients</p>
      <p class="brand__tagline">Quality Inputs for Industry</p>
    </div>
    <address class="contact contact--address">
      PT Varo Ingredients<br>
      Ruko Pelita Sumber Asri, Blok K07 no: 15-16<br>
      Cempaka Hijau Utara, 14590<br>
      Indonesia
    </address>
    <address class="contact contact--lines">
      Tel:+62 21 738 2096<br>
      Fax:+62 21 738 2097<br>
      Email: info@varo-ingredients.example<br>
      Website: www.varo-ingredients.example
    </address>
  </section>

  <section class="letterhead letterhead--rule" aria-label="Letterhead with red rules">
    <svg class="letterhead__art" viewBox="0 0 540 764" aria-hidden="true">
      <rect x="30" y="140" width="480" height="3" fill="var(--brand-red)"/>
      <rect x="80" y="150" width="360" height="1" fill="var(--brand-red)"/>
      <rect x="100" y="682" width="400" height="1" fill="var(--brand-red)"/>
      <rect x="0" y="692" width="540" height="3" fill="var(--brand-red)"/>
    </svg>
    <div class="brand">
      <p class="brand__name">Varo Ingredients</p>
      <p class="brand__tagline">Quality Inputs for Industry</p>
    </div>
    <address class="contact contact--address">
      PT Varo Ingredients<br>
      Ruko Pelita Sumber Asri, Blok K07 no: 15-16<br>
      Cempaka Hijau Utara, 14590<br>
      Indonesia
    </address>
    <address class="contact contact--lines">
      Tel:+62 21 738 2096<br>
      Fax:+62 21 738 2097<br>
      Email: info@varo-ingredients.example<br>
      Website: www.varo-ingredients.example
    </address>
  </section>

</body>
</html>
```